New company website for Redfern Hollow Builders

We're looking to build a new company website that customers can use to contact us, get quotes, view past projects (renovations, additions, new construction, etc.), & learn more about our business. We want to use WordPress for our website and have already purchased the Lumo theme (by Parcel Layouts). Using that theme isn't required but we already have several examples of websites that we want to model our site after that use this theme. The "look" we're after is simple, light, & clean.

Target Market(s)

Residential remodeling, renovations, and new construction.

Industry/Entity Type

Residential Construction

Coding

Coded - Design and coding required

Number of Pages Required

5+ page

Font styles to use
Sans Serif

Colors
33a6d7
aaaaaa

Requirements
Must have
• We require the website to be coded using the Lumo theme. We'll be upgrading the project to include this today or tomorrow.
• The navigation bar should be static & remain at the top of the page. When scrolling we'd like the logo & info in the nav bar to size down. Here's an example of a site that does this: https://qrvhomesite.example/
Nice to have
• In the gallery with pictures of our finished product/jobs, when you mouse over the image, we'd like there to be additional info that shows up. For example, look at this gallery: https://qrvhomesite.example/projectcategories/kitchens/ We'll add a name/location of the job like: "Brandt kitchen - Apex, N.C."
• If you go to this website: https://lornbuildworks.example/ and scroll down to the pictures, we like how the picture moves and is interactive.

```html
<!DOCTYPE html>
<html lang="en">
<head>
<meta charset="utf-8">
<title>Redfern Hollow Builders</title>
<link rel="stylesheet" href="https://fonts.googleapis.com/css2?family=Montserrat:wght@400;500;600;700&family=Open+Sans:wght@400;600&display=swap">
<style>
:root{
  --brand:#33a6d7;
  --brand-dark:#1f73c7;
  --grey:#aaaaaa;
  --icon:#6f6f6f;
  --text:#666666;
  --heading:#333333;
  --navy:#163f5a;
  --footer-bg:#f5f5f5;
  --white:#ffffff;
}
*{box-sizing:border-box;margin:0;padding:0}
html,body{width:1200px;height:2795px;overflow:hidden;background:var(--white)}
body{font-family:"Open Sans",sans-serif;color:var(--text);position:relative}
a{color:inherit;text-decoration:none}

/* header */
.site-header{position:absolute;top:0;left:0;width:1200px;height:106px;background:var(--white)}
.top-info{position:absolute;right:121px;top:24px;font-size:12px;color:#555;display:flex;gap:14px;align-items:center;white-space:nowrap}
.top-info span{display:flex;align-items:center;gap:4px}
.brand{position:absolute;left:110px;top:61px;font-family:"Montserrat",sans-serif;font-weight:700;font-size:19px;color:#555;letter-spacing:.5px;white-space:nowrap}
.main-nav{position:absolute;right:121px;top:67px;display:flex;gap:27px;font-family:"Montserrat",sans-serif;font-weight:500;font-size:13.5px;color:#555;align-items:center;white-space:nowrap}
.main-nav .current{color:var(--brand)}
.main-nav .drop::after{content:"";display:inline-block;width:5px;height:5px;border-right:1.5px solid #666;border-bottom:1.5px solid #666;transform:rotate(45deg);margin-left:7px;position:relative;top:-3px}

/* hero */
.hero{position:absolute;top:106px;left:0;width:1200px;height:462px;background:linear-gradient(100deg,#8b8580 0%,#a9a39d 35%,#7c7671 60%,#4e4a47 100%)}
.hero-shade{position:absolute;inset:0;background:rgba(0,0,0,.25)}
.hero h1{position:absolute;top:156px;width:100%;text-align:center;font-family:"Montserrat",sans-serif;font-weight:500;font-size:37px;color:var(--white)}
.hero-actions{position:absolute;top:268px;left:0;width:100%;display:flex;justify-content:center;gap:54px}
.btn{display:inline-flex;align-items:center;justify-content:center;text-align:center;white-space:nowrap;height:46px;padding:0;font-family:"Montserrat",sans-serif;font-weight:500;font-size:16px;color:var(--white);border:2px solid var(--white)}
.btn-outline{width:174px}
.btn-solid{width:184px;background:var(--brand-dark)}

/* features */
.features{position:absolute;top:568px;left:0;width:1200px;height:343px}
.feature{position:absolute;top:60px;width:300px;text-align:center}
.feature svg{display:block;margin:0 auto;height:56px}
.feature h3{margin-top:33px;font-family:"Montserrat",sans-serif;font-weight:500;font-size:19px;color:var(--brand);letter-spacing:.4px;white-space:nowrap}
.feature p{margin-top:10px;font-size:14px;line-height:25px;color:#777;padding:0 10px}

/* process */
.process{position:absolute;top:911px;left:0;width:1200px;height:607px;background:linear-gradient(135deg,#1e4d6b 0%,#2b5e7e 40%,#173e58 100%);color:var(--white);text-align:center}
.process h2{position:absolute;top:78px;width:100%;font-family:"Montserrat",sans-serif;font-weight:600;font-size:24px}
.process .intro{position:absolute;top:120px;left:106px;width:988px;font-family:"Montserrat",sans-serif;font-weight:500;font-size:14px;line-height:27px}
.step{position:absolute;top:220px;width:300px}
.step svg{display:block;margin:0 auto;height:50px}
.step h4{margin-top:24px;font-family:"Montserrat",sans-serif;font-weight:600;font-size:18px}
.step p{margin-top:10px;font-family:"Montserrat",sans-serif;font-weight:500;font-size:13.5px;line-height:26px}
.process .btn{position:absolute;top:452px;left:518px;width:148px;height:46px;font-size:15px}

/* specialties */
.specialties{position:absolute;top:1518px;left:0;width:1200px;height:729px}
.spec-intro{position:absolute;left:106px;top:72px;width:460px}
.spec-intro h2{font-family:"Montserrat",sans-serif;font-weight:600;font-size:25px;color:var(--brand)}
.spec-intro p{margin-top:12px;font-size:15px;line-height:26px;color:#666}
.spec-intro p+p{margin-top:18px}
.btn-portfolio{margin-top:28px;display:inline-flex;align-items:center;justify-content:center;white-space:nowrap;width:197px;height:44px;background:var(--brand);color:var(--white);font-family:"Montserrat",sans-serif;font-weight:500;font-size:15px}
.project{position:absolute;width:460px;height:293px;overflow:hidden}
.project .photo{position:absolute;inset:0}
.project .caption{position:absolute;width:322px;background:rgba(255,255,255,.82);padding:28px 28px}
.project h5{font-family:"Montserrat",sans-serif;font-weight:600;font-size:15px;color:var(--brand);letter-spacing:.5px}
.project p{margin-top:18px;font-size:13px;line-height:26px;color:#777}
.p-addition{left:619px;top:73px}
.p-addition .photo{background:linear-gradient(180deg,#d8d8d4 0%,#8c8a84 50%,#7a6a4a 100%)}
.p-addition .caption{left:138px;top:86px;height:173px;padding-top:24px}
.p-new{left:106px;top:388px}
.p-new .photo{background:linear-gradient(160deg,#f2f2f0 0%,#d9d9d6 50%,#5b6676 100%)}
.p-new .caption{left:0;top:86px;height:207px;padding-top:38px}
.p-remodel{left:619px;top:388px}
.p-remodel .photo{background:linear-gradient(160deg,#efefed 0%,#cfcfcc 55%,#6b6560 100%)}
.p-remodel .caption{left:138px;top:86px;height:207px;padding-top:38px}

/* footer */
.site-footer{position:absolute;top:2247px;left:0;width:1200px;height:499px;background:var(--footer-bg)}
.foot-brand{position:absolute;left:106px;top:58px;font-family:"Montserrat",sans-serif;font-weight:700;font-size:34px;color:#666;letter-spacing:1px;white-space:nowrap}
.foot-about{position:absolute;left:106px;top:125px;width:460px;font-size:12px;line-height:21px;color:#666}
.foot-contact{position:absolute;left:106px;top:256px;font-size:12px;line-height:21px;color:#666}
.foot-contact h6,.foot-col h6{font-family:"Montserrat",sans-serif;font-weight:600;font-size:15px;color:var(--brand);margin-bottom:9px;line-height:20px}
.foot-contact .line{display:flex;align-items:center;gap:5px}
.foot-col{position:absolute;width:220px}
.foot-col.narrow{width:165px}
.foot-col ul{list-style:none;font-size:12px;line-height:25px;color:#666}
.foot-col li::before{content:"";display:inline-block;width:5px;height:5px;border-radius:50%;background:var(--brand);margin-right:9px;position:relative;top:-2px}
.copybar{position:absolute;top:2746px;left:0;width:1200px;height:49px;background:var(--brand);color:var(--white)}
.copybar p{position:absolute;left:106px;top:16px;font-family:"Montserrat",sans-serif;font-weight:500;font-size:11px}
.social{position:absolute;right:121px;top:18px;display:flex;gap:20px}
.social span{width:12px;height:12px;border-radius:50%;background:var(--white)}
</style>
</head>
<body>

<header class="site-header">
  <div class="top-info">
    <span><svg width="10" height="10" viewBox="0 0 10 10"><path d="M2 1l2 2-1 1c.6 1.3 1.7 2.4 3 3l1-1 2 2-1.5 1.5C4.5 9 1 5.5.5 2.5z" fill="#666"/></svg>+1 555 010 2400</span>
    <span><svg width="11" height="8" viewBox="0 0 11 8"><rect width="11" height="8" fill="#666"/><path d="M0 0l5.5 4.5L11 0" stroke="#fff" fill="none"/></svg>info@redfernhollow.example</span>
  </div>
  <div class="brand">Redfern Hollow Builders</div>
  <nav class="main-nav">
    <a class="current">Home</a>
    <a class="drop">Getting Started</a>
    <a class="drop">Who We Are</a>
    <a class="drop">Specialties</a>
    <a class="drop">Portfolio</a>
    <a>Contact Us</a>
    <svg width="14" height="14" viewBox="0 0 14 14"><circle cx="8" cy="6" r="4.5" stroke="#666" stroke-width="1.6" fill="none"/><path d="M4.8 9.2L1 13" stroke="#666" stroke-width="1.8"/></svg>
  </nav>
</header>

<section class="hero" role="img" aria-label="Photo of a couple relaxing on a white sofa in a bright living room with a stone feature wall">
  <div class="hero-shade"></div>
  <h1>Redfern Hollow Builders</h1>
  <div class="hero-actions">
    <a class="btn btn-outline">Our Specialties</a>
    <a class="btn btn-solid">Get a free Quote</a>
  </div>
</section>

<section class="features">
  <div class="feature" style="left:150px">
    <svg viewBox="0 0 40 56" width="40"><circle cx="20" cy="18" r="14" fill="none" stroke="var(--icon)" stroke-width="4"/><circle cx="20" cy="18" r="7" fill="var(--icon)"/><path d="M11 29l-5 22 8-5 4 8 4-20M29 29l5 22-8-5-4 8-4-20" fill="var(--icon)"/></svg>
    <h3>Proven Trust</h3>
    <p>Home projects can be challenging. You need a company whose experience can lead to the result you want.</p>
  </div>
  <div class="feature" style="left:441px">
    <svg viewBox="0 0 60 50" width="58"><rect x="16" y="2" width="42" height="28" rx="6" fill="var(--icon)"/><rect x="2" y="14" width="42" height="28" rx="6" fill="var(--icon)" stroke="#fff" stroke-width="3"/><path d="M10 41l-2 8 10-7z" fill="var(--icon)"/><path d="M10 24h26M10 31h20" stroke="#fff" stroke-width="3"/></svg>
    <h3>Constant communication</h3>
    <p>Stay informed during every step of your project with your own SiteLedger account page.</p>
  </div>
  <div class="feature" style="left:782px">
    <svg viewBox="0 0 60 44" width="58"><path d="M2 8l14-6 12 6 10-4 20 8v16l-6 4-14 12-6-2-4 2-6-4-6-2L2 26z" fill="var(--icon)"/><path d="M24 18l10-4 12 10M20 30l6 4M26 26l8 6M32 22l8 6" stroke="#fff" stroke-width="2" fill="none"/></svg>
    <h3>History of Experience</h3>
    <p>We're focused on your goals and promise to always do what's best for you every step of the way.</p>
  </div>
</section>

<section class="process" role="img" aria-label="Background photo of a house interior under construction, tinted dark blue">
  <h2>Our Process</h2>
  <p class="intro">Nobody provides quality like Lorn. Whether the project is interior or exterior, addition or kitchen, half-bath or bedroom, we have the know-how to make it happen. Beautiful homes require brilliant thinking. Check out our latest insights, all inspired by client successes.</p>
  <div class="step" style="left:100px">
    <svg viewBox="0 0 50 46" width="50"><path d="M22 3C11 3 3 10 3 19c0 4 2 8 5 10l-3 9 10-5c2 .6 4 1 7 1 11 0 19-7 19-15S33 3 22 3z" fill="none" stroke="#fff" stroke-width="3"/><path d="M40 20c5 2 8 6 8 11 0 3-1 5-3 7l2 7-8-4" fill="none" stroke="#fff" stroke-width="3"/></svg>
    <h4>Step1</h4>
    <p>Meet to discuss your goals and give you a chance to ask as many questions as you'd like.</p>
  </div>
  <div class="step" style="left:442px">
    <svg viewBox="0 0 46 46" width="46"><rect x="3" y="9" width="34" height="34" fill="none" stroke="#fff" stroke-width="3"/><path d="M10 24l9 9L43 3" fill="none" stroke="#fff" stroke-width="4"/></svg>
    <h4>Step2</h4>
    <p>Agree on the strategy that works best for your situation and their need.</p>
  </div>
  <div class="step" style="left:785px">
    <svg viewBox="0 0 40 52" width="38"><path d="M20 3C11 3 4 10 4 19c0 6 3 10 7 13v7h18v-7c4-3 7-7 7-13C36 10 29 3 20 3z" fill="none" stroke="#fff" stroke-width="3"/><path d="M13 44h14M15 49h10" stroke="#fff" stroke-width="3"/></svg>
    <h4>Step3</h4>
    <p>Stay in frequent communication throughout so you don't miss an opportunity.</p>
  </div>
  <a class="btn">Get Started</a>
</section>

<section class="specialties">
  <div class="spec-intro">
    <h2>Our Specialities</h2>
    <p>Beautiful homes require brilliant thinking. Check out our latest insights, all inspired by client successes.</p>
    <p>Nobody provides quality like Lorn. Whether the project is interior or exterior, addition or kitchen, half-bath or bedroom, we have the know-how to make it happen.</p>
    <a class="btn-portfolio">View Our Portfolio</a>
  </div>
  <article class="project p-addition">
    <div class="photo" role="img" aria-label="Photo of a house exterior with a new addition among bare trees"></div>
    <div class="caption"><h5>Addition</h5><p>We're focused on your goals and promise to always do what's best for you every step of the way.</p></div>
  </article>
  <article class="project p-new">
    <div class="photo" role="img" aria-label="Photo of a bright new kitchen with pendant lights and navy cabinets"></div>
    <div class="caption"><h5>New home construction</h5><p>We're focused on your goals and promise to always do what's best for you every step of the way.</p></div>
  </article>
  <article class="project p-remodel">
    <div class="photo" role="img" aria-label="Photo of a remodeled living area with staircase, ceiling fan and wood floors"></div>
    <div class="caption"><h5>Remodeling</h5><p>We're focused on your goals and promise to always do what's best for you every step of the way.</p></div>
  </article>
</section>

<footer class="site-footer">
  <div class="foot-brand">Redfern Hollow Builders</div>
  <p class="foot-about">Interested in a design-build project? Fill out our form below and we'll be in touch within 24 hours. Thank you for your interest in Redfern Hollow Builders.</p>
  <div class="foot-contact">
    <h6>Contact Us</h6>
    <p>Redfern Hollow Builders<br>418 Alder Ridge Rd, Suite 210<br>Cedar Falls, TX 75900</p>
    <p class="line" style="margin-top:30px"><svg width="10" height="10" viewBox="0 0 10 10"><path d="M2 1l2 2-1 1c.6 1.3 1.7 2.4 3 3l1-1 2 2-1.5 1.5C4.5 9 1 5.5.5 2.5z" fill="#666"/></svg>+1 555 010 2400</p>
    <p class="line" style="margin-top:10px"><svg width="11" height="8" viewBox="0 0 11 8"><rect width="11" height="8" fill="#666"/><path d="M0 0l5.5 4.5L11 0" stroke="#fff" fill="none"/></svg>info@redfernhollow.example</p>
  </div>
  <div class="foot-col" style="left:619px;top:60px"><h6>Getting Started</h6><ul><li>What to expect</li><li>Our process</li><li>FAQs</li></ul></div>
  <div class="foot-col" style="left:619px;top:192px"><h6>Specialties</h6><ul><li>Remodeling</li><li>New home construction</li><li>Additions</li></ul></div>
  <div class="foot-col" style="left:619px;top:324px"><h6>Contact Us</h6><ul><li>Get Quotes</li><li>SiteLedger</li></ul></div>
  <div class="foot-col" style="left:876px;top:60px"><h6>Who We Are</h6><ul><li>Our story</li><li>Redfern Hollow team</li><li>Testimonials</li></ul></div>
  <div class="foot-col" style="left:876px;top:192px"><h6>Portfolio</h6><ul><li>Before and after</li><li>Kitchens</li><li>Bathrooms</li><li>Whole house</li></ul></div>
  <div class="foot-col narrow" style="left:876px;top:350px"><h6>Know Our Privacy Policy</h6><ul><li>Privacy Policy</li><li>Disclaimer</li></ul></div>
</footer>

<div class="copybar">
  <p>Copyright © 2018 Redfern Hollow Builders.</p>
  <div class="social"><span></span><span></span><span></span></div>
</div>

</body>
</html>
```